Sample Box for Collegiate Alumni Fundraising

We are a screen printing and embroidery company. Our core services are 1) printing & embroidery on apparel (t-shirts, hoodies etc) 2) promo products like mugs, stickers and 3) fulfillment (shipping orders to individuals that have placed orders.
I would like a sample box designed for our specific target market - College and university alumni giving offices. These offices are in charge of running fundraising campaigns. The two main types of campaigns are Giving Day (each school choses their own unique date but most are in the spring) and Lantern Crest (this is a set date each year which occurs the Tuesday after Thanksgiving). Many schools host their own day as well as participate in Lantern Crest. Oftentimes we are tasked with research and tracking down the right product for each campaign.
I have attached two examples that we had created for running clubs. I am open to both real photos or illustrations. I do not want to match these examples, I just want to demonstrate the general design of a sample box.
I do want to highlight our services on side panels like the examples. Printing, Fulfillment, Product Options

```html
<!DOCTYPE html>
<html lang="en">
<head>
<meta charset="utf-8">
<title>Alumni Care Sample Box – Dieline</title>
<link href="https://fonts.googleapis.com/css2?family=Ubuntu:ital,wght@0,400;0,700;1,700&family=Roboto+Slab:wght@700;800&family=Arimo:ital,wght@0,400;0,700;1,700&display=swap" rel="stylesheet">
<style>
  :root {
    --teal: #00b9a5;
    --teal-soft: #6ad9c8;
    --cream: #fcf3ee;
    --orange: #f9ae3a;
    --orange-text: #f28c1e;
    --blue: #3a7dc2;
    --flap-blue: #4586c8;
    --navy: #1f3566;
    --white: #ffffff;
    --blush: #f7d6cc;
  }
  html, body {
    margin: 0;
    padding: 0;
    width: 1200px;
    height: 924px;
    overflow: hidden;
    background: var(--white);
  }
  .dieline-sheet {
    display: block;
    width: 1200px;
    height: 924px;
  }
  .panel-cream { fill: var(--cream); stroke: var(--navy); stroke-width: 1.5; }
  .panel-teal { fill: var(--teal); stroke: var(--navy); stroke-width: 1.5; }
  .flap-blue { fill: var(--flap-blue); }
  .accent-band { fill: var(--orange); }
  .cut-line { fill: var(--white); stroke: var(--navy); stroke-width: 2; }
  .inside-teal { fill: var(--teal-soft); }
  .icon-slot { fill: var(--orange); opacity: 0.22; }
  .icon-slot-navy { fill: var(--navy); opacity: 0.15; }

  .side-title { font-family: "Ubuntu", sans-serif; font-weight: 700; font-size: 54px; fill: var(--blue); }
  .side-note { font-family: "Ubuntu", sans-serif; font-weight: 400; font-size: 17px; fill: var(--blue); }
  .lid-line { font-family: "Ubuntu", sans-serif; font-size: 31px; fill: var(--white); }
  .lid-line-strong { font-weight: 700; font-style: italic; }
  .brand-name { font-family: "Ubuntu", sans-serif; font-weight: 700; font-size: 24px; fill: var(--navy); }
  .hero-title { font-family: "Roboto Slab", serif; font-weight: 800; font-size: 122px; fill: var(--white); }
  .hero-sub { font-family: "Ubuntu", sans-serif; font-size: 34px; letter-spacing: 8px; fill: var(--white); }
  .hero-tag { font-family: "Arimo", sans-serif; font-size: 22px; fill: var(--white); }
  .hero-tag-strong { font-weight: 700; font-style: italic; }
  .service-label { font-family: "Arimo", sans-serif; font-weight: 700; font-size: 29px; fill: var(--blue); }
  .inside-line { font-family: "Ubuntu", sans-serif; font-size: 31px; fill: var(--navy); }
  .inside-accent { font-weight: 700; font-style: italic; fill: var(--orange); }
  .heart-line { font-family: "Arimo", sans-serif; font-size: 22px; fill: var(--orange-text); }
  .heart-line-strong { font-weight: 700; font-style: italic; }
</style>
</head>
<body>
<svg class="dieline-sheet" viewBox="0 0 2184 1680" xmlns="http://www.w3.org/2000/svg">

  <!-- ===== Outside print ===== -->
  <g class="outside-print">

    <!-- Welcome Packs flap -->
    <g class="panel-welcome">
      <rect class="panel-cream" x="263" y="68" width="580" height="185"/>
      <rect class="accent-band" x="263" y="237" width="580" height="9"/>
      <text class="side-title" x="310" y="146">Welcome</text>
      <text class="side-title" x="310" y="195">Packs</text>
      <text class="side-note" x="306" y="221" style="font-size:16px">shipped directly to new members</text>
      <rect class="icon-slot" x="668" y="76" width="156" height="156" rx="20" role="img" aria-label="Orange line icon of a t-shirt"/>
    </g>

    <!-- Lid -->
    <g class="panel-lid">
      <rect class="panel-teal" x="263" y="253" width="580" height="485"/>
      <rect x="365" y="416" width="82" height="70" fill="var(--navy)" opacity="0.85"/>
      <text class="brand-name" x="406" y="512" text-anchor="middle">Hollowbrook</text>
      <text class="brand-name" x="406" y="538" text-anchor="middle">Print Co.</text>
      <text class="lid-line" x="637" y="462" text-anchor="middle">Fast delivery.</text>
      <text class="lid-line lid-line-strong" x="637" y="493" text-anchor="middle">Certified Sustainable.</text>
      <rect x="492" y="646" width="138" height="36" rx="18" fill="var(--navy)" opacity="0.35"/>
    </g>

    <!-- Apparel Drops side -->
    <g class="panel-apparel">
      <rect class="panel-cream" x="60" y="256" width="197" height="481"/>
      <rect class="accent-band" x="243" y="256" width="10" height="481"/>
      <rect class="icon-slot" x="104" y="284" width="104" height="156" rx="20" role="img" aria-label="Orange line icon of a baseball cap"/>
      <text class="side-title" transform="translate(150 700) rotate(-90)">Apparel</text>
      <text class="side-title" transform="translate(198 700) rotate(-90)">Drops</text>
      <text class="side-note" transform="translate(226 700) rotate(-90)">new designs provided to keep things fresh</text>
    </g>

    <!-- Giving Support side -->
    <g class="panel-giving">
      <rect class="panel-cream" x="849" y="256" width="196" height="481"/>
      <rect class="accent-band" x="852" y="256" width="10" height="481"/>
      <text class="side-title" transform="translate(960 288) rotate(90)">Giving</text>
      <text class="side-title" transform="translate(906 288) rotate(90)">Support</text>
      <text class="side-note" transform="translate(878 293) rotate(90)">discounted volunteer shirt</text>
      <rect class="icon-slot" x="872" y="530" width="130" height="190" rx="20" role="img" aria-label="Orange line icon of two hands holding a heart"/>
    </g>

    <!-- Webstore front wall -->
    <g class="panel-webstore">
      <rect class="panel-cream" x="263" y="740" width="580" height="183"/>
      <rect class="accent-band" x="263" y="744" width="580" height="8"/>
      <rect class="icon-slot" x="288" y="760" width="164" height="130" rx="16" role="img" aria-label="Orange line icon of a web storefront with a shirt on a screen"/>
      <g transform="rotate(180 553 831)">
        <text class="side-title" x="296" y="854" style="font-size:50px">Webstore</text>
        <text class="side-note" x="296" y="878" style="font-size:16px">no setup fees, inventory required</text>
      </g>
    </g>

    <!-- Blue dust flaps -->
    <g class="dust-flaps">
      <path class="flap-blue" d="M257 927 L180 937 C110 948 72 1000 72 1060 L72 1260 C72 1330 120 1380 180 1385 L257 1390 Z"/>
      <path class="flap-blue" d="M257 1405 L72 1405 C72 1520 150 1585 257 1590 Z"/>
      <path class="flap-blue" d="M849 927 L926 937 C996 948 1032 1000 1032 1060 L1032 1260 C1032 1330 986 1380 926 1385 L849 1390 Z"/>
      <path class="flap-blue" d="M849 1405 L1032 1405 C1032 1520 956 1585 849 1590 Z"/>
    </g>

    <!-- Alumni Care base -->
    <g class="panel-alumni">
      <rect class="panel-teal" x="263" y="924" width="580" height="483"/>
      <defs>
        <linearGradient id="photo-tone" x1="0" y1="0" x2="1" y2="1">
          <stop offset="0" stop-color="#fbe4dc"/>
          <stop offset="0.6" stop-color="var(--blush)"/>
          <stop offset="1" stop-color="#fbe9e3"/>
        </linearGradient>
      </defs>
      <path d="M340 1052 C300 1050 276 1090 278 1150 C282 1250 315 1330 365 1407 L570 1407 C610 1360 630 1290 615 1240 C595 1180 555 1160 515 1150 C455 1135 420 1060 340 1052 Z"
            fill="url(#photo-tone)" role="img" aria-label="Photo of hands holding a graduation cap and a rolled diploma"/>
      <text class="hero-title" x="480" y="1070" textLength="336" lengthAdjust="spacingAndGlyphs">Alumni</text>
      <rect class="accent-band" x="480" y="1098" width="102" height="5"/>
      <rect class="accent-band" x="720" y="1098" width="98" height="5"/>
      <text class="hero-sub" x="655" y="1116" text-anchor="middle">CARE</text>
      <text class="hero-tag" x="830" y="1360" text-anchor="end">Empowering Your</text>
      <text class="hero-tag hero-tag-strong" x="830" y="1385" text-anchor="end">Giving Caimpaigns</text>
    </g>

    <!-- Services back wall -->
    <g class="panel-services">
      <rect class="panel-cream" x="263" y="1407" width="580" height="183"/>
      <text class="service-label" x="367" y="1500" text-anchor="middle">NO</text>
      <text class="service-label" x="367" y="1528" text-anchor="middle">INVENTORY</text>
      <rect x="466" y="1462" width="5" height="84" fill="var(--blue)"/>
      <text class="service-label" x="556" y="1500" text-anchor="middle">ONLINE</text>
      <text class="service-label" x="556" y="1528" text-anchor="middle">STORE</text>
      <rect x="647" y="1462" width="5" height="84" fill="var(--blue)"/>
      <text class="service-label" x="740" y="1500" text-anchor="middle">GIVING</text>
      <text class="service-label" x="740" y="1528" text-anchor="middle">SUPPORT</text>
    </g>
  </g>

  <!-- ===== Inside print ===== -->
  <g class="inside-print">
    <!-- Top flap with ears -->
    <path class="cut-line" d="M1368 68 L1300 68 C1230 70 1182 150 1182 230 C1182 245 1190 253 1205 253 L1368 253 Z"/>
    <path class="cut-line" d="M1946 68 L2010 68 C2080 70 2133 150 2133 230 C2133 245 2125 253 2110 253 L1946 253 Z"/>
    <rect class="cut-line" x="1368" y="68" width="578" height="185"/>

    <!-- Lid interior with side flaps -->
    <path class="cut-line" d="M1368 268 L1258 283 C1215 290 1184 330 1184 370 L1184 620 C1184 670 1215 705 1258 713 L1368 733 Z"/>
    <path class="cut-line" d="M1948 268 L2058 283 C2101 290 2133 330 2133 370 L2133 620 C2133 670 2101 705 2058 713 L1948 733 Z"/>
    <rect class="cut-line" x="1368" y="253" width="580" height="480"/>
    <rect class="icon-slot-navy" x="1484" y="432" width="332" height="58" rx="12" role="img" aria-label="Row of navy line icons: t-shirt, socks, cap, hoodie, medal"/>
    <text class="inside-line" x="1665" y="543" text-anchor="middle">Apparel design, production,</text>
    <text class="inside-line" x="1665" y="575" text-anchor="middle">and sales <tspan class="inside-accent">made simple.</tspan></text>

    <!-- Front wall -->
    <rect class="cut-line" x="1368" y="733" width="580" height="188"/>

    <!-- Base interior -->
    <rect class="cut-line" x="1172" y="923" width="196" height="480"/>
    <rect class="cut-line" x="1948" y="923" width="196" height="480"/>
    <rect class="inside-teal" x="1370" y="923" width="578" height="482"/>
    <path d="M1665 1060 C1600 980 1472 990 1472 1110 C1472 1200 1600 1280 1665 1345 C1730 1280 1857 1200 1857 1110 C1857 990 1730 980 1665 1060 Z" fill="var(--white)"/>
    <text class="heart-line" x="1668" y="1137" text-anchor="middle">We handle the details</text>
    <text class="heart-line heart-line-strong" x="1668" y="1164" text-anchor="middle">You can make many peoples</text>
    <text class="heart-line heart-line-strong" x="1668" y="1191" text-anchor="middle">lives better</text>

    <!-- Back wall -->
    <rect class="cut-line" x="1368" y="1407" width="580" height="186"/>
  </g>

  <rect class="accent-band" x="2179" y="0" width="5" height="1680"/>
</svg>
</body>
</html>
```